Bottled Margarita Label Project

We need a label design (using a 750 ml bottle) for an all natural, premium, Ready to Drink (as in pre-mixed) Margarita. The brand is called VONDRA Pure Margarita. We were tired of the chemical, sugary, preservative laden "margaritas" with artificial colorings and cheap tequilas, so we developed a simple, straightforward CLASSIC, ingredient driven margarita made with only the purest, traditional ingredients: 100% Blue Agave Tequila Reposado, Double Distilled Orange Liqueur, Lime Juice and sweetened with Organic Cane Sugar. The result is a pure margarita, the kind you got on that amazing beach vacation in Mexico. This is a product that can be chilled and served over ice or straight up. You might grab one to take to a BBQ or to the beach. It's simple, sexy and classic. We are hoping the final design can communicate purity, integrity of ingredients and the freedom one might feel when on vacation in the sun. This doesnt have to be a Latin themed beverage, but more of a Summer / chill / "sala del oro" in a bottle vibe. Thank you!

Target Market(s)

25 to 45 year olds who feel they know what makes up a good margarita. Aspirational types who love adventurous vacations but are not necessarily wealthy. Our customer doesn't always have the time to make a real margarita from scratch but wish they could get a decent one in a bottle that doesn't taste artificial. They are brand and label conscious and will pay a little more for quality as long as there is value.

Industry/Entity Type

Cafe

Requirements
Must have
• Must have "Vondra" and "pure margartia" clearly listed as the name of the beverage. Must also make clear that this is "Premium", "Ready to Drink" and "Made with 100% Blue Agave Tequila"
Nice to have
• We really love designs that are clean and uncluttered. We have imagined a clear 750ml bottle. Think about tequila when you think about this label. This is a hand made, artisan product produced in batches. We are looking for a finished label/bottle that is colorful, transcendent, artisinal and timeless. It should be mature but not stuffy. It should be simple and sexy - not splashy, brash or silly. Our competition is Tidy Moth Margarita, Rafa Tolentes, and Brevo pre-mixed margaritas which are fake margaritas made in huge factories. Vondra is made with integrity and honest ingredients. For colors, greens come to mind but we are totally open to a designer's vision ;). This should be a product that a fashion forward airline like Halcyon Skyways would want serve and a bottle that a savvy drinker would choose over the bland, mainstream brands. Check out Munrez Cachaça for a sexy, vibrant take on a bottle of alcohol with a Summer slant. Also look at Velquiro tequila. They have a wonderful label that blends vintage and modern elements with minimalist design and comes off as handmade.
Should not have
• Elements we do NOTwant to see any red colors, sombreros, parrots, tiki masks, palm trees, spring break, deserted islands, or Dale Hornsby imagery. This should be a product that an airline like Halcyon Skyways would want to serve.

```html
<!DOCTYPE html>
<html lang="en">
<head>
<meta charset="utf-8">
<title>Vondra Pure Margarita – Label Colourways</title>
<link rel="stylesheet" href="https://fonts.googleapis.com/css2?family=Cormorant+Garamond:wght@500;700&display=swap">
<style>
  :root {
    --stage: #1d1e1f;
    --paper: #ffffff;
    --lime: #5d9a3c;
    --lime-deep: #2f4a1c;
    --lime-tint: #dcebc9;
    --agave-gold: #a0902e;
    --agave-gold-deep: #5a4a10;
    --agave-gold-tint: #efe9c4;
    --dusk: #5b5a8c;
    --dusk-deep: #2b2a55;
    --dusk-tint: #dedcf0;
    --premium: #a98a2c;
    --ready: #7a6a3a;
  }
  html, body {
    margin: 0;
    padding: 0;
    overflow: hidden;
  }
  body {
    width: 1200px;
    height: 1000px;
    background: var(--stage);
    position: relative;
  }
  .label {
    position: absolute;
  }
  .label svg {
    display: block;
    width: 100%;
    height: auto;
  }
  .label--lime { --ink: var(--lime); --ink-deep: var(--lime-deep); --tint: var(--lime-tint); left: 375px; top: 70px; width: 750px; }
  .label--gold { --ink: var(--agave-gold); --ink-deep: var(--agave-gold-deep); --tint: var(--agave-gold-tint); left: 385px; top: 605px; width: 345px; }
  .label--dusk { --ink: var(--dusk); --ink-deep: var(--dusk-deep); --tint: var(--dusk-tint); left: 658px; top: 710px; width: 315px; }

  .label-serif { font-family: "Cormorant Garamond", serif; }
</style>
</head>
<body>

<div class="label label--lime">
  <svg viewBox="0 0 760 470" aria-label="Vondra Pure Margarita label, green">
    <defs>
      <linearGradient id="paper-lime" x1="0" y1="0" x2="0" y2="1">
        <stop offset="0" style="stop-color:var(--tint)"/>
        <stop offset="0.5" style="stop-color:var(--paper)"/>
        <stop offset="1" style="stop-color:var(--tint)"/>
      </linearGradient>
    </defs>
    <rect class="label-shape" x="10" y="10" width="740" height="450" rx="34" fill="url(#paper-lime)"/>
    <rect class="label-top-band" x="10" y="40" width="740" height="14" style="fill:var(--ink)"/>
    <text class="label-serif" x="712" y="100" text-anchor="end" font-size="18" font-weight="500" letter-spacing="2" style="fill:var(--premium)">PREMIUM</text>
    <circle cx="205" cy="190" r="14" style="fill:var(--ink)"/>
    <text class="label-serif" x="395" y="225" text-anchor="middle" font-size="110" font-weight="700" style="fill:var(--ink)">Vondra</text>
    <rect class="label-rule" x="160" y="262" width="440" height="3" style="fill:var(--ink)"/>
    <text class="label-serif" x="380" y="322" text-anchor="middle" font-size="50" font-weight="700" letter-spacing="2" style="fill:var(--ink-deep)">Pure Margarita</text>
    <text class="label-serif" x="380" y="364" text-anchor="middle" font-size="18" font-weight="500" letter-spacing="10" style="fill:var(--ready)">Ready to Drink</text>
    <rect class="label-band" x="10" y="388" width="740" height="40" style="fill:var(--ink)"/>
    <text class="label-serif" x="380" y="415" text-anchor="middle" font-size="20" font-weight="500" letter-spacing="1" fill="#ffffff">Made with 100% BLUE AGAVE TEQUILA</text>
  </svg>
</div>

<div class="label label--gold">
  <svg viewBox="0 0 760 470" aria-label="Vondra Pure Margarita label, gold">
    <defs>
      <linearGradient id="paper-gold" x1="0" y1="0" x2="0" y2="1">
        <stop offset="0" style="stop-color:var(--tint)"/>
        <stop offset="0.5" style="stop-color:var(--paper)"/>
        <stop offset="1" style="stop-color:var(--tint)"/>
      </linearGradient>
    </defs>
    <rect class="label-shape" x="10" y="10" width="740" height="450" rx="40" fill="url(#paper-gold)"/>
    <rect class="label-top-band" x="10" y="40" width="740" height="14" style="fill:var(--ink)"/>
    <text class="label-serif" x="712" y="100" text-anchor="end" font-size="24" font-weight="500" letter-spacing="2" style="fill:var(--premium)">PREMIUM</text>
    <circle cx="205" cy="190" r="14" style="fill:var(--ink)"/>
    <text class="label-serif" x="395" y="225" text-anchor="middle" font-size="110" font-weight="700" style="fill:var(--ink)">Vondra</text>
    <rect class="label-rule" x="160" y="262" width="440" height="4" style="fill:var(--ink)"/>
    <text class="label-serif" x="380" y="322" text-anchor="middle" font-size="52" font-weight="700" letter-spacing="2" style="fill:var(--ink-deep)">Pure Margarita</text>
    <text class="label-serif" x="380" y="366" text-anchor="middle" font-size="24" font-weight="500" letter-spacing="10" style="fill:var(--ready)">Ready to Drink</text>
    <rect class="label-band" x="10" y="388" width="740" height="42" style="fill:var(--ink)"/>
    <text class="label-serif" x="380" y="417" text-anchor="middle" font-size="24" font-weight="500" letter-spacing="1" fill="#ffffff">Made with 100% BLUE AGAVE TEQUILA</text>
  </svg>
</div>

<div class="label label--dusk">
  <svg viewBox="0 0 760 470" aria-label="Vondra Pure Margarita label, violet">
    <defs>
      <linearGradient id="paper-dusk" x1="0" y1="0" x2="0" y2="1">
        <stop offset="0" style="stop-color:var(--tint)"/>
        <stop offset="0.5" style="stop-color:var(--paper)"/>
        <stop offset="1" style="stop-color:var(--tint)"/>
      </linearGradient>
    </defs>
    <rect class="label-shape" x="10" y="10" width="740" height="450" rx="40" fill="url(#paper-dusk)"/>
    <rect class="label-top-band" x="10" y="40" width="740" height="14" style="fill:var(--ink)"/>
    <text class="label-serif" x="712" y="100" text-anchor="end" font-size="24" font-weight="500" letter-spacing="2" style="fill:var(--premium)">PREMIUM</text>
    <circle cx="205" cy="190" r="14" style="fill:var(--ink)"/>
    <text class="label-serif" x="395" y="225" text-anchor="middle" font-size="110" font-weight="700" style="fill:var(--ink)">Vondra</text>
    <rect class="label-rule" x="160" y="262" width="440" height="4" style="fill:var(--ink)"/>
    <text class="label-serif" x="380" y="322" text-anchor="middle" font-size="52" font-weight="700" letter-spacing="2" style="fill:var(--ink-deep)">Pure Margarita</text>
    <text class="label-serif" x="380" y="366" text-anchor="middle" font-size="24" font-weight="500" letter-spacing="10" style="fill:var(--ready)">Ready to Drink</text>
    <rect class="label-band" x="10" y="388" width="740" height="42" style="fill:var(--ink)"/>
    <text class="label-serif" x="380" y="417" text-anchor="middle" font-size="24" font-weight="500" letter-spacing="1" fill="#ffffff">Made with 100% BLUE AGAVE TEQUILA</text>
  </svg>
</div>

</body>
</html>
```